依頼詳細
●デザインの要望
・少し温かみ、やわらかさのあるデザイン(まるっこすぎない)
※参考例:poruくらいのやわらかさ
・そのほかの色については特に指定なし(現在の青は入れなくてOKです)
⇒カラフルにするかどうかもデザインの中で考えて頂いて結構です
・現在のアプリにある下記のボタンを全て実装する
※投稿ボタン、画面更新ボタン、履歴ボタン、オプションボタン、カテゴリ選択ボタン の5個
・投稿が表示されるマス目は正方形だけでなく長方形等もまぜてほしい
※現在は正方形オンリーですが、縦に2個くっつけたものや横に2個くっつけたものが入ってきたりするデザイン
⇒アプリ:Tiledeck の記事一覧画面のようなイメージ
・zelvonなのでzvos7のフラットなイメージ(がっつり立体的にはしてほしくないです)

●納品物
PSDファイル1個(zelvonで使用する倍のサイズの 1920x1280 くらいで作ってください)
可能であればレイヤーのあるPNGファイル(可能であればで結構です)

サイトURL
https://apps.trovenlo.jp/jp/app/id518203764?mt=8
ページ数
1ページ
希望イメージ
シンプル 複雑
単色 カラフル
暗い 明るい
日常 高級
遊び心 厳粛
未来的 伝統的
女性的 男性的
希望する色
小豆色や薄い茶色等温かみのある色全般
納品ファイル
• フォトショップ形式 (.psd)
• PNG形式 (.png)
補足説明
■ 選んだ理由

やわらかいテイストでかつ既存の青をさし色に入れて頂けたこと、
またプラスアルファとしてスプラッシュスクリーンをご提示いただけたため、
より実装後のアプリのイメージがわくことができました。

■ 提案者全員のお礼・コメント

たくさんのご提案ありがとうございました。
特にUIそのものまで提案して頂けたりと非常にこちらとしても勉強になる案件となりました。

上部のバーのデザインや、吹き出し型のデザイン、カラフル、マット等
かなり悩ませていただきました。
最終的にはより女性的で、かつ落ち着いている
という部分を基準に選ぶことにしました。

本アプリは今後もどんどん改良を加える予定のため、
また機会が有りましたら是非宜しくお願い致します。

```html
<!DOCTYPE html>
<html lang="ja">
<head>
<meta charset="utf-8">
<title>yomu タイル一覧</title>
<link rel="stylesheet" href="https://fonts.googleapis.com/css2?family=M+PLUS+1p:wght@400;500;700&display=swap">
<style>
  :root {
    --ad-bar: #8c8c8c;
    --header-bg: #ffffff;
    --grid-gap: #e2e0df;
    --tile-white: #ffffff;
    --salmon: #f3816f;
    --peach: #f6c08e;
    --slate: #7e7e80;
    --ash: #a3a3a5;
    --text-pink: #ec6f63;
    --text-gray: #8a8786;
    --toolbar: #3b3b3d;
    --white: #ffffff;
  }
  * { box-sizing: border-box; margin: 0; padding: 0; }
  html, body {
    width: 800px; height: 1200px; overflow: hidden;
    background: var(--grid-gap);
    font-family: "M PLUS 1p", sans-serif;
  }
  .screen { position: relative; width: 800px; height: 1200px; overflow: hidden; }

  .ad-bar {
    position: absolute; left: 0; top: 0; width: 800px; height: 75px;
    background: var(--ad-bar); color: var(--white);
    font-size: 22px; padding: 22px 16px; letter-spacing: 1px;
  }

  .app-header {
    position: absolute; left: 0; top: 75px; width: 800px; height: 106px;
    background: var(--header-bg);
  }
  .brand {
    position: absolute; left: 18px; top: 36px;
    font-size: 30px; font-weight: 400; line-height: 1; color: var(--text-pink);
    letter-spacing: 3px;
  }

  .category-tabs { position: absolute; right: 6px; top: 32px; display: flex; gap: 6px; }
  .tab {
    width: 56px; height: 54px; display: flex; align-items: center; justify-content: center;
    text-align: center; font-size: 19px; line-height: 1.1; color: var(--white);
  }
  .tab--all { background: var(--white); color: var(--text-gray); border: 2px solid #d6d6d6; }
  .tab--love { background: var(--peach); }
  .tab--people { background: var(--salmon); font-size: 17px; }
  .tab--anger { background: var(--slate); }
  .tab--r20 { background: var(--ash); }

  .tile-grid { position: absolute; left: 0; top: 181px; width: 800px; height: 912px; overflow: hidden; }
  .tile {
    position: absolute; padding: 14px 14px; overflow: hidden;
    font-size: 22px; line-height: 1.45; letter-spacing: .5px;
  }
  .tile--white { background: var(--tile-white); color: var(--text-pink); }
  .tile--white.is-muted { color: var(--text-gray); }
  .tile--salmon { background: var(--salmon); color: var(--white); }
  .tile--peach { background: var(--peach); color: var(--white); }

  .toolbar {
    position: absolute; left: 0; top: 1093px; width: 800px; height: 107px;
    background: var(--toolbar);
  }
  .toolbar-button { position: absolute; top: 30px; width: 48px; height: 48px; }
</style>
</head>
<body>
<div class="screen">
  <div class="ad-bar">広告スペース</div>

  <header class="app-header">
    <div class="brand">yomu</div>
    <nav class="category-tabs">
      <div class="tab tab--all">全体</div>
      <div class="tab tab--love">恋愛</div>
      <div class="tab tab--people">人間<br>関係</div>
      <div class="tab tab--anger">怒り</div>
      <div class="tab tab--r20">R20</div>
    </nav>
  </header>

  <main class="tile-grid">
    <div class="tile tile--salmon" style="left:-100px;top:0;width:222px;height:433px;">朝から外に出して祖母…一先見えば寒いからサイズをもう一度見て行こう…それで…何とか入れてすがらだけ</div>
    <div class="tile tile--white" style="left:127px;top:0;width:222px;height:214px;">寒い季節はチョコが美味しくてほんと困りますね…</div>
    <div class="tile tile--white" style="left:354px;top:0;width:222px;height:214px;">乾燥からかしてすごいほっぺが乾いてかゆい…でもほんとひりひりする。</div>
    <div class="tile tile--white" style="left:581px;top:0;width:222px;height:214px;">そういえば、先日MMRワクチン接種したことを話してたら、子供のワクチン接種の話に。</div>

    <div class="tile tile--white is-muted" style="left:127px;top:219px;width:222px;height:214px;">王女と魔法の約束素敵だった〜〜。けどずっとカエルだったから私には辛かった（笑）</div>
    <div class="tile tile--white is-muted" style="left:354px;top:219px;width:222px;height:214px;">苦いね。時間が解決してくれるとも限らないけれど、時間が解決してくれると思えない。</div>
    <div class="tile tile--white is-muted" style="left:581px;top:219px;width:222px;height:214px;">缶コーヒーの「レギュラーに寄せてはいるけど、単純にイマイチ」という商品。</div>

    <div class="tile tile--white" style="left:-100px;top:438px;width:222px;height:214px;">部署異動決まった〜!!!</div>
    <div class="tile tile--white" style="left:127px;top:438px;width:449px;height:214px;">うちの旦那は洋服を機内持ち込みしようとしてC4と勘違いされ、仕方がないのでその場で食ったら「こいつ要領良いわ」と大爆笑になったという伝説を持っている</div>
    <div class="tile tile--salmon" style="left:581px;top:438px;width:222px;height:433px;">こんなにボールを一日中でもボールを追いかけて、ボールがいつでも側にあって、次の日もまた同じように朝からボールを待っている。そんな毎日が少しだけうらやましいと思う。</div>

    <div class="tile tile--salmon" style="left:-100px;top:657px;width:222px;height:214px;">欲しいのはチョコで鍋の具材を買って帰る予定の日曜日。</div>
    <div class="tile tile--peach" style="left:127px;top:657px;width:222px;height:214px;">雨の中で鍋の具材を買って帰って、仕事終わりに少し、目の保養になった〜</div>
    <div class="tile tile--white is-muted" style="left:354px;top:657px;width:222px;height:214px;">息子の学校でもインフル流行ってて、11時半に帰宅させますと連絡が来た</div>

    <div class="tile tile--white" style="left:-100px;top:876px;width:222px;height:214px;">完全にイメージです</div>
    <div class="tile tile--peach" style="left:127px;top:876px;width:222px;height:214px;">なう(・ω・)</div>
    <div class="tile tile--white is-muted" style="left:354px;top:876px;width:222px;height:214px;">俺の時間がピーアンビ</div>
    <div class="tile tile--white" style="left:581px;top:876px;width:222px;height:214px;">殺愛なる君よ 今でも本</div>
  </main>

  <footer class="toolbar">
    <svg class="toolbar-button" style="left:131px" viewBox="0 0 48 48" aria-label="投稿">
      <path d="M8 40 L11 29 L33 7 L41 15 L19 37 Z" fill="#fff"/>
      <path d="M8 40 L11 29 L19 37 Z" fill="#3b3b3d" opacity=".35"/>
    </svg>
    <svg class="toolbar-button" style="left:291px" viewBox="0 0 48 48" aria-label="更新">
      <path d="M38 24 A14 14 0 1 1 30 11" fill="none" stroke="#fff" stroke-width="5" stroke-linecap="round"/>
      <path d="M26 4 L38 10 L28 19 Z" fill="#fff"/>
    </svg>
    <svg class="toolbar-button" style="left:440px" viewBox="0 0 48 48" aria-label="履歴">
      <path d="M10 4 H29 L39 14 V44 H10 Z" fill="none" stroke="#fff" stroke-width="4" stroke-linejoin="round"/>
      <path d="M29 4 V14 H39" fill="none" stroke="#fff" stroke-width="4" stroke-linejoin="round"/>
    </svg>
    <svg class="toolbar-button" style="left:595px" viewBox="0 0 48 48" aria-label="オプション">
      <g fill="#fff">
        <circle cx="24" cy="24" r="13"/>
        <rect x="20" y="3" width="8" height="10"/>
        <rect x="20" y="35" width="8" height="10"/>
        <rect x="3" y="20" width="10" height="8"/>
        <rect x="35" y="20" width="10" height="8"/>
        <rect x="20" y="3" width="8" height="10" transform="rotate(45 24 24)"/>
        <rect x="20" y="3" width="8" height="10" transform="rotate(135 24 24)"/>
        <rect x="20" y="3" width="8" height="10" transform="rotate(225 24 24)"/>
        <rect x="20" y="3" width="8" height="10" transform="rotate(315 24 24)"/>
      </g>
      <circle cx="24" cy="24" r="5" fill="#3b3b3d"/>
    </svg>
  </footer>
</div>
</body>
</html>
```